Brennick Holdings Business Cards

These are professional business cards that are for my family office.
Put fake emails and phone numbers as of now until I finalize those components. This family office controls my families investments, assets, and future. The cards should be professional.
..
.
.
.
I just uploaded another variation of a logo I would like to see as a business card to I am inbeteen which logo to use

Target Market(s)

business

Industry/Entity Type

business

Contact Information for Business Card

Professional, wealth related, finance related.

Requirements
Must have
• Logo

```html
<!DOCTYPE html>
<html lang="en">
<head>
<meta charset="UTF-8">
<title>Brennick Holdings Business Cards</title>
<link rel="stylesheet" href="https://fonts.googleapis.com/css2?family=Cinzel:wght@600&family=Inter:wght@500;600&display=swap">
<style>
  :root {
    --backdrop: #e0e0e0;
    --navy: #171d29;
    --paper: #fafbfb;
    --ink: #171d29;
    --title-grey: #a8a8a8;
    --contact-grey: #6b6b6b;
    --white: #ffffff;
  }
  * { margin: 0; padding: 0; box-sizing: border-box; }
  html, body {
    width: 1200px;
    height: 1200px;
    overflow: hidden;
    background: var(--backdrop);
  }
  .card {
    position: absolute;
    left: 179px;
    width: 861px;
    height: 496px;
  }
  .card-front {
    top: 84px;
    background: var(--navy);
    display: flex;
    align-items: center;
    justify-content: center;
  }
  .card-back {
    top: 622px;
    background: var(--paper);
    text-align: center;
  }
  .front-wordmark {
    font-family: "Cinzel", serif;
    font-weight: 600;
    font-size: 40px;
    letter-spacing: 0.04em;
    color: var(--white);
  }
  .back-wordmark {
    position: absolute;
    left: 0;
    right: 0;
    top: 74px;
    font-family: "Cinzel", serif;
    font-weight: 600;
    font-size: 42px;
    letter-spacing: 0.02em;
    color: var(--ink);
    line-height: 1;
  }
  .holder-name {
    position: absolute;
    left: 0;
    right: 0;
    top: 207px;
    font-family: "Inter", sans-serif;
    font-weight: 600;
    font-size: 31px;
    letter-spacing: 0.06em;
    color: var(--ink);
    line-height: 1.2;
  }
  .holder-title {
    position: absolute;
    left: 0;
    right: 0;
    top: 243px;
    font-family: "Inter", sans-serif;
    font-weight: 600;
    font-size: 27px;
    letter-spacing: 0.03em;
    color: var(--title-grey);
    line-height: 1.2;
  }
  .contact-list {
    position: absolute;
    left: 0;
    right: 0;
    top: 341px;
    list-style: none;
    font-family: "Inter", sans-serif;
    font-weight: 500;
    font-size: 26px;
    letter-spacing: 0.14em;
    color: var(--contact-grey);
    line-height: 36.5px;
  }
</style>
</head>
<body>
  <section class="card card-front">
    <span class="front-wordmark">Brennick Holdings</span>
  </section>

  <section class="card card-back">
    <h1 class="back-wordmark">Brennick Holdings</h1>
    <p class="holder-name">ADRIAN CALLOWAY</p>
    <p class="holder-title">Founder</p>
    <ul class="contact-list">
      <li>800-555-0147</li>
      <li>office@brennickhq.com</li>
      <li>www.brennickhq.com</li>
    </ul>
  </section>
</body>
</html>
```